Summit Crest Advisory - White Collar Engineering Consultancy

I'm chasing a website to provide high level information about what Summit Crest Advisory is and service's we provide - only chasing something simple. We are a new white collar secondment/contractor/professional services/consultancy specialising is providing the best consultants into contractor roles.

Our primary industries are energy, gas, pipelines, water processing, power, projects, geographic information systems, design, accounting.

Our people are mechanical,/electrical/civil/process/chemical engineers, project engineers, project managers, technical experts, GIS analysts, integrity engineers, pipeline engineers,

Currently I have this domain registered through nimbledns - https://www.scadvisoryhub.com/

I'd like to keep this domain but completely overhaul the website to be sleek and follow the logo styling.

Example websites within my industry that I like:
- https://www.bramwellfieldworks.com.au/
- https://quorvin.com.au/
- https://www.hlmtec.com.au/

I'd like the winner to code and assist with making the website functional under my domain.

Would like to include:
- industries
- services
- why work with us
- terms and conditions as per attached
- location (Brisbane)
- contact us form, that submits an email to jordan.pryce@scadvisoryhub.com
- WorkCircle link

Would definitely be looking to polish the winning result with the designer over the phone or via email.

I will also add some infrastructure photos for use; otherwise please use generic CSG related infrastructure.

Cheers,

Jordan

Industry/Entity Type

Energy, resources, gas, mining, geographic information systems, accounting, construction.

Coding

Coded - Design and coding required

Number of Pages Required

4 page

Colors
0054AA
0677BA
7BADD7
CADEEF
E8F1F8

Requirements
Must have
• Refer to project description

```html
<!DOCTYPE html>
<html lang="en">
<head>
<meta charset="utf-8">
<title>Summit Crest Advisory</title>
<link href="https://fonts.googleapis.com/css2?family=Inter:wght@300;400;500;600&display=swap" rel="stylesheet">
<style>
:root{
  --navy-deep:#11163d;
  --navy:#1d2250;
  --paper:#eff0eb;
  --mist:#eeeff3;
  --line:#d4d6df;
  --muted:#6b6f86;
  --white:#ffffff;
  --stage:#e2e2e4;
}
*{box-sizing:border-box;margin:0;padding:0}
html,body{width:1200px;height:3337px;overflow:hidden}
body{background:var(--stage);font-family:"Inter",Arial,sans-serif;color:var(--navy-deep)}
.site{position:absolute;left:160px;top:30px;width:880px;background:var(--white)}
.wrap{padding:0 25px}
.eyebrow{font-size:7px;letter-spacing:2.4px;text-transform:uppercase;color:var(--muted)}
h2{font-weight:500;font-size:26px;letter-spacing:-.3px;color:var(--navy)}
p{line-height:1.55}

/* top bar */
.topbar{height:24px;display:flex;align-items:stretch;margin:0 25px;border-bottom:1px solid var(--navy);font-size:7px;color:var(--navy)}
.topbar div{display:flex;align-items:center;padding:0 10px;border-left:1px solid var(--navy);border-right:1px solid var(--navy)}
.topbar .addr{margin-left:auto;margin-right:auto;width:210px;justify-content:center}
.topbar .follow{gap:10px}
.topbar .sq{width:8px;height:8px;background:var(--navy)}

/* nav */
.nav{height:52px;display:flex;align-items:center;padding:0 25px}
.brand{display:flex;align-items:center;gap:6px;font-size:15px;font-weight:600;color:var(--navy)}
.brand i{width:17px;height:17px;border-radius:50%;background:var(--navy);display:block}
.nav ul{list-style:none;display:flex;gap:40px;margin-left:auto;margin-right:42px;font-size:9px;color:var(--navy)}
.btn-dark{background:var(--navy);color:var(--white);font-size:8.5px;font-weight:500;padding:10px 18px}

/* hero */
.hero{margin:0 25px;height:428px;position:relative;background:linear-gradient(180deg,#a9b6cb 0%,#c6cbd6 45%,#8c93a0 78%,#4d5364 100%)}
.hero h1{position:absolute;left:65px;top:60px;font-weight:500;font-size:32px;line-height:1.1;color:var(--navy)}
.hero h1 span{color:var(--white)}
.hero p{position:absolute;left:82px;top:182px;width:350px;font-size:8.5px;color:var(--white);padding-left:16px;border-left:1px solid var(--white)}
.dots{position:absolute;right:24px;top:366px;display:flex;flex-direction:column;gap:7px}
.dots i{width:8px;height:8px;border:1px solid var(--white);border-radius:50%}
.dots i.on{background:var(--white)}

/* about */
.about{height:302px;position:relative}
.about h2{position:absolute;left:25px;top:56px}
.about .lead{position:absolute;left:25px;top:102px;width:205px;font-size:10px;line-height:1.5;color:var(--navy)}
.stat{position:absolute;left:372px;display:flex;align-items:flex-start;gap:10px}
.stat:before{content:"";width:45px;height:1px;background:var(--navy);margin-top:22px}
.stat b{display:block;font-weight:500;font-size:40px;line-height:1;color:var(--navy)}
.stat small{display:block;font-size:7.5px;margin-top:6px}
.about .side{position:absolute;left:648px;top:102px;width:210px;font-size:8px;color:var(--muted)}

/* services */
.services{margin:0 25px;height:331px;background:var(--navy);position:relative;color:var(--white)}
.services .eyebrow{position:absolute;left:40px;top:64px;color:#b7bad0}
.services h2{position:absolute;left:40px;top:78px;color:var(--white);font-size:25px}
.svc{position:absolute;width:190px;display:flex;gap:14px}
.svc svg{flex:none}
.svc h3{font-weight:500;font-size:13px;margin-bottom:6px}
.svc p{font-size:8px;color:#c5c8da}

/* industries */
.industries{height:432px;position:relative;overflow:hidden}
.industries .eyebrow{position:absolute;left:25px;top:64px}
.industries h2{position:absolute;left:25px;top:78px}
.arrows{position:absolute;right:25px;top:88px;display:flex;gap:8px;font-size:14px;color:var(--navy)}
.arrows span:first-child{color:#a4a7b8}
.cards{position:absolute;left:25px;top:137px;display:flex;gap:14px}
.sliver{position:absolute;left:0;top:137px;width:12px;height:230px;background:var(--white);box-shadow:0 6px 18px rgba(17,22,61,.08)}
.card{width:220px;height:230px;background:var(--white);box-shadow:0 6px 18px rgba(17,22,61,.08);padding:13px 14px}
.card .ph{height:111px;background:linear-gradient(180deg,#b8c6d8,#7d8799)}
.card h3{font-weight:500;font-size:11.5px;margin:12px 7px 6px}
.card p{font-size:7.5px;color:var(--muted);margin:0 7px}
.card .go{display:block;margin:8px 7px 0;font-size:12px;color:var(--navy)}
.card.active{background:var(--navy);color:var(--white)}
.card.active p,.card.active .go{color:#d0d2e0}

/* values */
.values{height:410px;background:var(--mist);position:relative}
.values .eyebrow{position:absolute;left:25px;top:66px}
.values h2{position:absolute;left:25px;top:80px}
.values .txt{position:absolute;left:25px;top:130px;width:255px;font-size:8px;color:var(--muted)}
.btn-line{position:absolute;left:25px;top:205px;border:1px solid var(--navy);font-size:7px;padding:8px 15px;color:var(--navy)}
.accordion{position:absolute;left:400px;top:66px;width:456px;height:280px;background:var(--white);padding:24px 35px;list-style:none}
.accordion li{display:flex;justify-content:space-between;font-size:8px;color:var(--navy);padding:12px 0 10px;border-bottom:1px solid var(--line)}
.accordion li:last-child{border:none}

/* process */
.process{height:413px;position:relative}
.process .ph{position:absolute;inset:0;background:linear-gradient(90deg,#e0e1ee 0%,#cfd2e3 35%,#a7aec4 60%,#c7ccdc 100%)}
.process .eyebrow{position:absolute;left:25px;top:72px;color:var(--white)}
.process h2{position:absolute;left:25px;top:86px;width:330px;font-size:27px;line-height:1.12}
.process p{position:absolute;left:25px;top:202px;width:330px;font-size:8.5px;color:var(--muted)}
.play{position:absolute;left:30px;top:267px;width:72px;height:72px;border-radius:50%;background:var(--white);box-shadow:0 0 0 10px rgba(255,255,255,.35);display:flex;align-items:center;justify-content:center}

/* contact */
.contact{height:530px;position:relative}
.contact .eyebrow{position:absolute;left:25px;top:64px}
.contact h2{position:absolute;left:25px;top:78px}
form{position:absolute;left:25px;top:125px;width:370px}
label{display:block;font-size:7px;margin-bottom:6px}
.field{border:1px solid #b9bccb;height:33px;margin-bottom:28px}
.row{display:flex;gap:15px}.row>div{flex:1}
.field.tall{height:88px}
.btn-submit{display:inline-block;background:var(--navy);color:var(--white);font-size:7.5px;padding:9px 15px;margin-top:-10px}
.map{position:absolute;left:465px;top:130px;width:345px;height:330px;background:radial-gradient(ellipse at 50% 45%,#e4e6ed 0%,#eff0f4 60%,var(--white) 80%)}
.map svg{position:absolute;left:330px;top:140px}
.map address{position:absolute;left:92px;top:250px;font-style:normal;font-size:8.5px;color:var(--muted);line-height:1.4}

/* footer */
.footer{height:353px;background:var(--navy);color:var(--white);position:relative}
.footer .brand{position:absolute;left:25px;top:60px;color:var(--white)}
.footer .brand i{background:var(--white)}
.fcol{position:absolute;top:56px;font-size:7.5px;line-height:1.9}
.fcol h4{font-weight:400;font-size:7px;color:#9da1c0;margin-bottom:6px}
.news{position:absolute;left:516px;top:183px;width:343px}
.news h4{font-weight:400;font-size:7px;color:#9da1c0;margin-bottom:8px}
.news .in{height:33px;background:#2a2f63;display:flex;align-items:center;justify-content:space-between;padding-left:15px;font-size:7.5px}
.news .in span:last-child{width:33px;height:33px;background:var(--white);display:flex;align-items:center;justify-content:center}
.legal{position:absolute;left:25px;right:25px;top:293px;display:flex;justify-content:space-between;font-size:6.5px;color:#c5c8da}
</style>
</head>
<body>
<main class="site">
  <div class="topbar">
    <div>jordan.pryce@scadvisoryhub.com</div>
    <div class="addr">Level 9/52 Harlow St, Brisbane City QLD 4000, Australia</div>
    <div class="follow">Follow Us: <span class="sq"></span></div>
  </div>

  <nav class="nav">
    <div class="brand"><i></i>Summit Crest Advisory</div>
    <ul><li>Home</li><li>About Us</li><li>Industries</li><li>Services</li><li>Why Work With Us</li></ul>
    <span class="btn-dark">Contact Us</span>
  </nav>

  <section class="hero" role="img" aria-label="Gas processing plant towers against a pale sky">
    <h1>Pioneering White Collar<br>Engineering <span>Solutions</span> &amp;<br><span>Consulting Services</span></h1>
    <p>Discover our trailblazing white-collar engineering solutions, where innovation, expertise, and dedication meet excellence in addressing complex modern industry challenges head on.</p>
    <div class="dots"><i></i><i class="on"></i><i></i></div>
  </section>

  <section class="about">
    <h2>About Us</h2>
    <p class="lead">We stand as a premier firm specializing in secondment, contractor placement, professional services, and consultancy. Our commitment to excellence drives our mission of linking the top-tier consultants with contractor positions spanning diverse industries.</p>
    <div class="stat" style="top:84px"><div><b>13+</b><small>Years of Experience</small></div></div>
    <div class="stat" style="top:163px"><div><b>504</b><small>Completed Projects</small></div></div>
    <p class="side">At Summit Crest Advisory, we believe that the right people can make all the difference in the success of a project or an organization. We take pride in being the link that connects talented professionals with opportunities where they can thrive.</p>
  </section>

  <section class="services">
    <div class="eyebrow">Our Services</div>
    <h2>What We Do</h2>
    <div class="svc" style="left:320px;top:62px">
      <svg width="40" height="42" viewBox="0 0 40 42" fill="none" stroke="#9da1c0" stroke-width="1.5"><path d="M20 2 37 11v20L20 40 3 31V11z"/><path d="M20 9l11 6v12l-11 6-11-6V15z"/></svg>
      <div><h3>Planning</h3><p>We help you chart a clear path forward by setting objectives, resource allocation, and outlining actionable steps.</p></div>
    </div>
    <div class="svc" style="left:600px;top:62px">
      <svg width="40" height="42" viewBox="0 0 40 42" fill="none" stroke="#9da1c0" stroke-width="1.5"><path d="M32 6A18 18 0 1 0 32 36"/><path d="M28 12A10 10 0 1 0 28 30"/></svg>
      <div><h3>Advisory</h3><p>We offer insightful guidance and tailored recommendations to help you navigate challenges and seize opportunities.</p></div>
    </div>
    <div class="svc" style="left:320px;top:186px">
      <svg width="40" height="42" viewBox="0 0 40 42" fill="none" stroke="#9da1c0" stroke-width="1.5"><path d="M20 4 38 38H2z"/><path d="M20 14 30 32H10z"/></svg>
      <div><h3>Project Management</h3><p>We bring efficiency, structure, and accountability to every endeavor, so you can focus on your project's success and more.</p></div>
    </div>
    <div class="svc" style="left:600px;top:186px">
      <svg width="40" height="42" viewBox="0 0 40 42" fill="none" stroke="#9da1c0" stroke-width="1.5"><path d="M2 14h12l8 18 8-18h8"/></svg>
      <div><h3>Design</h3><p>We transform your vision into compelling &amp; user-friendly solutions that stand out in today's competitive landscape.</p></div>
    </div>
  </section>

  <section class="industries">
    <div class="eyebrow">How We Work</div>
    <h2>Industries We Serve</h2>
    <div class="arrows"><span>&larr;</span><span>&rarr;</span></div>
    <div class="sliver"></div>
    <div class="cards">
      <article class="card"><div class="ph" role="img" aria-label="Oil and gas refinery site"></div><h3>Oil &amp; Gas</h3><p>Lorem ipsum dolor sit amet, consectetur scing elit, sed do eiusmod tempor incididunt ut et labore et dolore magna aliqua.</p><span class="go">&rarr;</span></article>
      <article class="card active"><div class="ph" role="img" aria-label="Water processing plant basins"></div><h3>Water Processing</h3><p>Lorem ipsum dolor sit amet, consectetur scing elit, sed do eiusmod tempor incididunt ut et labore et dolore magna aliqua.</p><span class="go">&rarr;</span></article>
      <article class="card"><div class="ph" role="img" aria-label="High voltage power transmission tower"></div><h3>Power &amp; Energy</h3><p>Lorem ipsum dolor sit amet, consectetur scing elit, sed do eiusmod tempor incididunt ut et labore et dolore magna aliqua.</p><span class="go">&rarr;</span></article>
      <article class="card"><div class="ph" role="img" aria-label="Industrial pipelines"></div><h3>Pipelines</h3><p>Lorem ipsum dolor sit amet, consectetur scing elit, sed do eiusmod tempor incididunt ut et labore et dolore magna aliqua.</p><span class="go">&rarr;</span></article>
    </div>
  </section>

  <section class="values">
    <div class="eyebrow">Why Choose Us</div>
    <h2>Core Values</h2>
    <p class="txt">Our commitment to excellence is grounded in a set of core values that guide our actions and define our identity. These values shape our interactions with clients, ensuring that we provide the highest level of service and maintain the integrity.</p>
    <span class="btn-line">Be a Partner</span>
    <ul class="accordion">
      <li>Client-Centric Approach<span>+</span></li>
      <li>Diversity and Inclusion<span>+</span></li>
      <li>Collaboration<span>+</span></li>
      <li>Innovation<span>+</span></li>
      <li>Integrity<span>+</span></li>
      <li>Adaptability<span>+</span></li>
    </ul>
  </section>

  <section class="process">
    <div class="ph" role="img" aria-label="Engineer reviewing designs on a glass board"></div>
    <div class="eyebrow">The Process</div>
    <h2>Unveiling the Mechanics of SCA: A Deeper Dive into How We Operate</h2>
    <p>Our commitment to excellence is grounded in a set of core values that guide our actions and define our identity. These values shape our interactions with clients, ensuring that we provide the highest level of service and maintain.</p>
    <div class="play"><svg width="16" height="18" viewBox="0 0 16 18"><path d="M2 1l13 8-13 8z" fill="#11163d"/></svg></div>
  </section>

  <section class="contact">
    <div class="eyebrow">Contact Us</div>
    <h2>Get in Touch</h2>
    <form>
      <label>Full Name*</label><div class="field"></div>
      <div class="row"><div><label>Phone*</label><div class="field"></div></div><div><label>Phone*</label><div class="field"></div></div></div>
      <label>Organisation*</label><div class="field"></div>
      <label>Message*</label><div class="field tall"></div>
      <span class="btn-submit">Submit Form</span>
    </form>
    <div class="map" role="img" aria-label="Map of Australia marking Brisbane">
      <svg width="10" height="14" viewBox="0 0 10 14"><path d="M5 0a5 5 0 0 1 5 5c0 4-5 9-5 9S0 9 0 5a5 5 0 0 1 5-5z" fill="#11163d"/><circle cx="5" cy="5" r="2" fill="#fff"/></svg>
      <address>Level 9/52 Harlow St,<br>Brisbane City QLD 4000,<br>Australia</address>
    </div>
  </section>

  <footer class="footer">
    <div class="brand"><i></i>Summit Crest Advisory</div>
    <div class="fcol" style="left:420px"><h4>Company</h4>About<br>Why Choose Us</div>
    <div class="fcol" style="left:516px"><h4>Industries</h4>Oil and Gas<br>Pipelines<br>Water Processing<br>Energy and Power<br>GIS</div>
    <div class="fcol" style="left:623px"><h4>Services</h4>Engineering<br>Planning<br>Civil Engineering<br>Audit &amp; Inspection</div>
    <div class="fcol" style="left:731px"><h4>Get in Touch</h4>jordan.pryce@scadvisoryhub.com<br>Brisbane</div>
    <div class="news"><h4>Subscribe to Newsletter</h4>
      <div class="in"><span>Enter Your Email Address</span><span><svg width="12" height="12" viewBox="0 0 12 12" fill="none" stroke="#1d2250"><path d="M1 6 11 1 8 11 6 7z"/></svg></span></div>
    </div>
    <div class="legal"><span>&copy; 2023 Summit Crest Advisory</span><span>Privacy Policy | Terms of Use</span><span>WorkCircle</span></div>
  </footer>
</main>
</body>
</html>
```